Powerpoint Template Design

We need a Corporate Powerpoint Template. We are a small boutique IT consultancy specialized in Business Intelligence and Analytics. We typically carry out projects and system implementations for our clients in Singapore and South East Asia region.
You may think: IT, arggg boring folks. No, we're not. We appreciate stylish design.
Attached is our logo that should appear in all slides, larger scale on the title slide and small size in content slides.

Industry/Entity Type

Boutique

```html
<!DOCTYPE html>
<html lang="en">
<head>
<meta charset="utf-8">
<title>Clearspan — Title Slide</title>
<link rel="stylesheet" href="https://fonts.googleapis.com/css2?family=Roboto+Condensed:wght@300;400&family=Fira+Sans:wght@500&display=swap">
<style>
  :root {
    --bg-top: #808080;
    --bg-mid: #ffffff;
    --bg-bottom: #c4c4c4;
    --brand-grey: #6f6f6f;
    --title-blue: #0f3d6e;
    --subtitle-grey: #9c9c9c;
    --band-light: #6496c8;
    --band-mid: #527fa9;
    --band-deep: #43709b;
    --wedge-top: #31639a;
    --wedge-bottom: #1d3757;
  }
  html, body {
    margin: 0;
    padding: 0;
    overflow: hidden;
  }
  .slide {
    position: relative;
    width: 1200px;
    height: 900px;
    overflow: hidden;
    background: linear-gradient(to bottom, var(--bg-top) 0%, var(--bg-mid) 55%, var(--bg-bottom) 82%);
  }
  .brand {
    position: absolute;
    left: 78px;
    top: 98px;
    margin: 0;
    font-family: "Fira Sans", sans-serif;
    font-weight: 500;
    font-size: 50px;
    letter-spacing: 0.5px;
    color: var(--brand-grey);
  }
  .title-block {
    position: absolute;
    left: 0;
    top: 208px;
    width: 1118px;
    text-align: center;
    font-family: "Roboto Condensed", sans-serif;
  }
  .title {
    margin: 0;
    font-weight: 400;
    font-size: 54px;
    line-height: 66px;
    color: var(--title-blue);
  }
  .subtitle {
    margin: 14px 0 0;
    font-weight: 300;
    font-size: 52px;
    line-height: 66px;
    color: var(--subtitle-grey);
  }
  .base-bands {
    position: absolute;
    left: 0;
    bottom: 0;
    width: 1200px;
    height: 900px;
  }
</style>
</head>
<body>
  <main class="slide">
    <p class="brand">Clearspan</p>

    <header class="title-block">
      <h1 class="title">Presentation name</h1>
      <p class="subtitle">text text text text text text text</p>
    </header>

    <svg class="base-bands" viewBox="0 0 1200 900" aria-hidden="true">
      <defs>
        <linearGradient id="wedge-fill" x1="0.4" y1="0" x2="0.7" y2="1">
          <stop offset="0" stop-color="var(--wedge-top)"/>
          <stop offset="1" stop-color="var(--wedge-bottom)"/>
        </linearGradient>
      </defs>
      <polygon class="band band-light" points="0,621 640,844 640,900 0,900" fill="var(--band-light)"/>
      <polygon class="band band-mid" points="0,664 640,887 640,900 0,900" fill="var(--band-mid)"/>
      <polygon class="band band-deep" points="0,738 480,905 0,905" fill="var(--band-deep)"/>
      <polygon class="wedge" points="1200,619 1200,900 70,900" fill="url(#wedge-fill)"/>
    </svg>
  </main>
</body>
</html>
```